Hopscotch Nell needs updated Marketing Material!

Moving business to a new location and am looking to update all marketing material, including business cards, postcards, flyers, website. I've attached a copy of my current business card.
Updates

Good Morning!  I just received my new business phone number.  It is 583-402-9176

Hello All Designers!

Thank you for all the submissions I have received so far!  I wanted to give you a bit more background on what Hopscotch Nell is all about:

I started this service when I was downsized out of a sales and marketing position.   A friend asked if I had time to run a few errands for her while she was at work.  "Lightbulb"!  I thought there must be more people that are over worked, over booked and want nothing more to do when they get home than spend time with their families or just relaxing.  And who wants to do all their running around on the weekends??  Hopscotch Nell was born!

I have been extremely fortunate with my business here in California.  However, this summer I will be moving to a small town in Pennsylvania and I will be in uncharted territory.  I hope to have marketing material that will "WOW" all new potential clients.  Letting them know that I offer a unique service that can put time back into their week and free up their weekends for more important things.

If there is anything else I can tell you in order to help you with your design process, please let me know!
Thank you!
Nellie

Target Market(s)

Busy working parents and young professionals with disposable income that would like to spend their down time doing things that they enjoy rather than doing errands.

Industry/Entity Type

Marketing

```html
<!DOCTYPE html>
<html lang="en">
<head>
<meta charset="utf-8">
<title>Hopscotch Nell – Business Card</title>
<link rel="stylesheet" href="https://fonts.googleapis.com/css2?family=Cabin:wght@400;600;700&display=swap">
<style>
  :root {
    --backdrop: #e8e5e2;
    --card-white: #f7f7f6;
    --brand-blue: #253a94;
    --brand-yellow: #e9e03a;
    --brand-magenta: #d61f5e;
    --ink-dark: #2a2a2a;
    --ink-light: #e6e8f2;
    --swirl-tone: #1d2f7c;
  }
  html, body {
    margin: 0;
    padding: 0;
    width: 1200px;
    height: 997px;
    overflow: hidden;
    background: var(--backdrop);
    font-family: "Cabin", "Gill Sans", sans-serif;
  }
  .canvas {
    position: relative;
    width: 1200px;
    height: 997px;
  }
  .card {
    position: absolute;
    top: 350px;
    width: 520px;
    height: 297px;
    box-shadow: 0 2px 6px rgba(0,0,0,0.12);
    overflow: hidden;
  }

  /* Back side */
  .card-back {
    left: 60px;
    background: var(--brand-blue);
  }
  .service-list {
    position: absolute;
    left: 32px;
    top: 40px;
    margin: 0;
    padding: 0;
    list-style: none;
    color: var(--ink-light);
    font-size: 15px;
    line-height: 21px;
    letter-spacing: 0.3px;
  }
  .service-list li::before {
    content: "";
    display: inline-block;
    width: 6px;
    height: 6px;
    margin-right: 8px;
    border-radius: 50%;
    background: var(--brand-yellow);
    vertical-align: middle;
  }
  .tagline {
    position: absolute;
    left: 32px;
    bottom: 34px;
    margin: 0;
    color: var(--brand-yellow);
    font-size: 22px;
    font-weight: 700;
    line-height: 25px;
  }
  .swirl-area {
    position: absolute;
    right: 0;
    top: 90px;
    width: 230px;
    height: 110px;
    background: linear-gradient(200deg, var(--swirl-tone), rgba(29,47,124,0));
    border-radius: 60px 0 0 60px;
    opacity: 0.7;
  }

  /* Front side */
  .card-front {
    left: 620px;
    background: var(--card-white);
  }
  .business-name {
    position: absolute;
    right: 26px;
    top: 22px;
    text-align: right;
  }
  .business-name h1 {
    margin: 0;
    font-size: 34px;
    font-weight: 400;
    color: var(--ink-dark);
    line-height: 36px;
  }
  .business-name p {
    margin: 2px 0 0;
    font-size: 12px;
    color: var(--ink-dark);
    letter-spacing: 0.2px;
  }
  .brand-mark {
    position: absolute;
    left: 70px;
    top: 132px;
  }
  .contact {
    position: absolute;
    left: 236px;
    top: 122px;
  }
  .contact-name {
    margin: 0 0 14px;
    font-size: 21px;
    font-weight: 700;
    color: var(--brand-magenta);
  }
  .contact-line {
    margin: 0;
    font-size: 14px;
    line-height: 18px;
    color: var(--brand-blue);
  }
  .contact-web {
    margin: 4px 0 0;
    font-size: 18px;
    font-weight: 700;
    color: var(--brand-blue);
  }
</style>
</head>
<body>
<main class="canvas">

  <section class="card card-back" aria-label="Business card, back">
    <ul class="service-list">
      <li>Personal Shopping and Errans</li>
      <li>Household Management</li>
      <li>Corporate Concierge</li>
      <li>Project Managment</li>
      <li>Group Rates for Teachers and Seniors</li>
    </ul>
    <div class="swirl-area" role="img" aria-label="Flowing decorative swirl lines"></div>
    <p class="tagline">We hop around so<br>you don't have to!</p>
  </section>

  <section class="card card-front" aria-label="Business card, front">
    <div class="business-name">
      <h1>Hopscotch Nell</h1>
      <p>Personal Concierge and Errand Service</p>
    </div>
    <svg class="brand-mark" width="120" height="120" viewBox="0 0 120 120" role="img" aria-label="Hopscotch Nell brand mark">
      <circle cx="60" cy="60" r="56" fill="var(--brand-blue)"/>
    </svg>
    <div class="contact">
      <p class="contact-name">Nellie Harlow</p>
      <p class="contact-line">583.402.9176</p>
      <p class="contact-line">nellie@hopscotchnell.biz</p>
      <p class="contact-web">www.hopscotchnell.biz</p>
    </div>
  </section>

</main>
</body>
</html>
```